We need a simple but upscale web site designed in word press.
A new breed boutique Investment Bank. Specializing in select cutting-edge emerging growth company financings with a focus on impact investing.
This is a customer facing site that must instill confidence,be clean, streamline and easy to navigate.

Target Market(s)

Entrepreneurs, Finance professionals, Investors

Industry/Entity Type

Bank

Number of Pages Required

5+ page

Font styles to use
Other font styles liked:
• see attached

Requirements
Must have
• Landing page
• About us
• Investors
• Entrepreneurs
• CrowdFunding
• Contact
Nice to have
• Sign up
• Similar look and feel to this site - https://tarnwickcapital.example

```html
<!DOCTYPE html>
<html lang="en">
<head>
<meta charset="utf-8">
<title>Brightfold Capital</title>
<link href="https://fonts.googleapis.com/css2?family=Mulish:wght@400;600;700;800&display=swap" rel="stylesheet">
<style>
:root{
  --blue:#1a72bb;
  --blue-dark:#0f5c9c;
  --green:#7cc242;
  --ink:#333;
  --muted:#8a8a8a;
  --rule:#d8d8d8;
  --grey-band:#f1f1f1;
  --footer:#58585a;
  --footer-text:#e6e6e6;
  --white:#fff;
}
*{box-sizing:border-box;margin:0;padding:0}
html,body{width:1200px;height:2778px;overflow:hidden}
body{font-family:"Mulish",Arial,sans-serif;color:var(--ink);background:var(--white);position:relative}
.abs{position:absolute}

/* header */
.site-header{position:absolute;top:0;left:0;width:1200px;height:93px;background:var(--white)}
.brand{position:absolute;left:185px;top:32px;display:flex;align-items:center;gap:10px;color:var(--blue);font-weight:600;font-size:17px;letter-spacing:.3px;white-space:nowrap}
.brand-dot{width:28px;height:28px;border:2px solid var(--blue);border-radius:50%;flex:none}
.main-nav{position:absolute;top:0;left:0}
.main-nav a{position:absolute;top:39px;font-size:14px;color:var(--ink);text-decoration:none;transform:translateX(-50%);white-space:nowrap}
.main-nav a.active{top:19px;width:58px;height:58px;border:2px solid var(--blue);border-radius:50%;display:flex;align-items:center;justify-content:center;color:var(--blue)}

/* hero */
.hero{position:absolute;top:93px;left:0;width:1200px;height:507px;background:linear-gradient(135deg,#6b5443 0%,#a88b6e 40%,#8a6e57 65%,#4d3b30 100%)}
.hero-shade{position:absolute;inset:0;background:rgba(30,25,20,.25)}
.hero h1{position:absolute;top:174px;width:100%;text-align:center;color:var(--white);font-weight:800;font-size:43px;letter-spacing:1px}
.hero h2{position:absolute;top:228px;width:100%;text-align:center;color:var(--white);font-weight:600;font-size:29px;letter-spacing:1px}
.btn-outline{position:absolute;border:2px solid var(--white);color:var(--white);font-size:14px;display:flex;align-items:center;justify-content:center}
.hero .btn-outline{left:532px;top:287px;width:144px;height:37px}
.slider-dots{position:absolute;top:469px;left:0;width:100%;display:flex;justify-content:center;gap:9px}
.slider-dots span{width:13px;height:13px;border-radius:50%;background:var(--white)}
.slider-dots span.current{background:transparent;border:2px solid var(--white)}

/* section headings */
.section-title{position:absolute;width:100%;text-align:center;color:var(--blue);font-size:28px;font-weight:400}

/* crowdfunding cards */
.card{position:absolute;top:702px;width:272px;height:289px;border:1px solid var(--rule);background:var(--white);box-shadow:0 1px 3px rgba(0,0,0,.08)}
.card-img{height:141px}
.card h3{margin:14px 18px 0;color:var(--blue);font-size:16px;font-weight:700}
.card p{margin:6px 18px 0;color:var(--muted);font-size:10.5px;line-height:1.45}
.progress{margin:18px 18px 0;height:6px;background:#ddd;border-radius:3px;overflow:hidden}
.progress i{display:block;height:100%;background:var(--green)}
.card-stats{margin:8px 18px 0;display:flex;justify-content:space-between;font-size:11px;text-align:center;color:#555;line-height:1.35}
.arrow{position:absolute;top:826px}

/* about band */
.about-band{position:absolute;top:1041px;left:0;width:1200px;height:366px;background:linear-gradient(180deg,#3a8bd0 0%,#1f75bf 55%,#1a67ac 100%)}
.about-band h2{position:absolute;top:62px;width:100%;text-align:center;color:var(--white);font-weight:400;font-size:31px}
.about-band p{position:absolute;left:250px;width:700px;text-align:center;color:var(--white);font-size:14px;line-height:1.6}
.about-band .btn-outline{left:543px;top:266px;width:122px;height:34px;font-size:12px;font-weight:700}

/* how it works */
.step-title{position:absolute;font-size:18px;color:var(--ink);text-align:center;width:280px;transform:translateX(-50%)}
.step-text{position:absolute;font-size:11px;color:var(--muted);text-align:center;width:200px;line-height:1.45;transform:translateX(-50%)}

/* investors */
.investors{position:absolute;top:1789px;left:0;width:1200px;height:322px;background:var(--grey-band);border-top:1px solid #e2e2e2;border-bottom:1px solid #e2e2e2}
.investors h2{position:absolute;top:44px;width:100%;text-align:center;font-weight:400;font-size:26px;color:#333}
.partner{position:absolute;transform:translate(-50%,-50%);color:#8c8c8c;font-size:19px;font-weight:600;white-space:nowrap}

/* testimonial */
.portrait{position:absolute;left:240px;top:2213px;width:160px;height:160px;border-radius:50%;border:3px solid #e4e4e4;background:linear-gradient(160deg,#c9d6e0,#8fa2b2)}
.quote-mark{position:absolute;color:var(--blue);font-size:42px;font-weight:800;line-height:1}
.quote-text{position:absolute;left:433px;top:2236px;width:460px;font-size:14px;line-height:1.75;color:#555}
.author{position:absolute;left:433px;top:2322px;font-size:15px;font-weight:600;color:#333}
.city{position:absolute;left:433px;top:2348px;font-size:14px;color:#555}

/* footer */
.site-footer{position:absolute;top:2456px;left:0;width:1200px;height:322px;background:var(--footer);color:var(--footer-text)}
.footer-col{position:absolute;top:56px}
.footer-col h4{font-size:17px;font-weight:600;color:var(--white);margin-bottom:14px}
.footer-col li{list-style:none;font-size:13.5px;line-height:26.5px}
.footer-brand{position:absolute;left:765px;top:152px;display:flex;align-items:center;gap:12px;color:#8f8f91;font-size:21px;font-weight:600;letter-spacing:1px;white-space:nowrap}
.footer-brand .brand-dot{border-color:#8f8f91;width:36px;height:36px}
.footer-rule{position:absolute;top:261px;left:185px;width:825px;height:1px;background:#6e6e70}
.footer-bottom{position:absolute;top:281px;font-size:12px;color:#d0d0d0}
</style>
</head>
<body>

<header class="site-header">
  <div class="brand"><span class="brand-dot"></span>BRIGHTFOLD CAPITAL</div>
  <nav class="main-nav">
    <a class="active" style="left:495px">Home</a>
    <a style="left:571px">About us</a>
    <a style="left:653px">Investors</a>
    <a style="left:752px">Entrepreneurs</a>
    <a style="left:871px">Crowdfunding</a>
    <a style="left:978px">Contactus</a>
  </nav>
</header>

<section class="hero" role="img" aria-label="Photo of a desk with glasses, coffee and investment notes being written">
  <div class="hero-shade"></div>
  <h1>CUM SOCIS NATOQUE PENATIBUS</h1>
  <h2>PRAESENT ELEMENTUM ELIT AT TELLUS</h2>
  <div class="btn-outline">Get Started</div>
  <div class="slider-dots"><span class="current"></span><span></span><span></span><span></span></div>
</section>

<h2 class="section-title" style="top:638px">Crowd Funding</h2>

<svg class="arrow" style="left:144px" width="24" height="34" viewBox="0 0 24 34"><path d="M18 3 5 17l13 14" fill="none" stroke="#aaa" stroke-width="3"/></svg>
<svg class="arrow" style="left:1038px" width="24" height="34" viewBox="0 0 24 34"><path d="M6 3l13 14L6 31" fill="none" stroke="#aaa" stroke-width="3"/></svg>

<article class="card" style="left:185px">
  <div class="card-img" role="img" aria-label="Photo of a modern office building" style="background:linear-gradient(180deg,#7fa7cf,#c8d3dc 60%,#9aa7b1)"></div>
  <h3>Tittle goes here</h3>
  <p>Maecenas aliquet velit vel turpis Mauris neque metus malesuada nec ultricies sit amet</p>
  <div class="progress"><i style="width:50%"></i></div>
  <div class="card-stats"><span>50%<br>Funded</span><span>£250.50<br>Raised</span><span>20<br>Days left</span></div>
</article>
<article class="card" style="left:469px">
  <div class="card-img" role="img" aria-label="Photo of a businessman in a suit with a city skyline" style="background:linear-gradient(135deg,#3e4a5a,#9aa9b8 50%,#e8d9c4)"></div>
  <h3>Tittle goes here</h3>
  <p>Maecenas aliquet velit vel turpis Mauris neque metus malesuada nec ultricies sit amet</p>
  <div class="progress"><i style="width:80%"></i></div>
  <div class="card-stats"><span>80%<br>Funded</span><span>£250.50<br>Raised</span><span>20<br>Days left</span></div>
</article>
<article class="card" style="left:752px">
  <div class="card-img" role="img" aria-label="Photo of hands holding a coffee cup and a tablet" style="background:linear-gradient(135deg,#3b3630,#8d7c6a 55%,#c9c3bb)"></div>
  <h3>Tittle goes here</h3>
  <p>Maecenas aliquet velit vel turpis Mauris neque metus malesuada nec ultricies sit amet</p>
  <div class="progress"><i style="width:50%"></i></div>
  <div class="card-stats"><span>50%<br>Funded</span><span>£250.50<br>Raised</span><span>20<br>Days left</span></div>
</article>

<section class="about-band" role="img" aria-label="Blue tinted photo of city office towers">
  <h2>Brightfold Capital</h2>
  <p style="top:122px">Maecenas aliquet velit vel turpis Mauris neque metus malesuada nec ultricies sit amet porttitor mattis enim In massa libero interdum nec interdum vel</p>
  <p style="top:171px">blandit sed nulla In ullamcorper est eget tempor cursus neque mi consectetuer mi a ultricies massa est sed nisl Class aptent taciti sociosqu ad litora torquent per conubia nostra per inceptos hymenaeos Proin nulla arcu nonummy luctus dictum eget fermentum et lorem Nunc porta</p>
  <div class="btn-outline">READ MORE</div>
</section>

<h2 class="section-title" style="top:1441px">How it Works</h2>

<svg class="abs" style="left:0;top:1480px" width="1200" height="280" viewBox="0 1480 1200 280">
  <line x1="365" y1="1590" x2="550" y2="1660" stroke="#c4c4c4" stroke-width="4"/>
  <line x1="650" y1="1660" x2="835" y2="1590" stroke="#c4c4c4" stroke-width="4"/>
  <g fill="#fff" stroke="#d4d4d4" stroke-width="3">
    <circle cx="320" cy="1556" r="60"/><circle cx="600" cy="1678" r="60"/><circle cx="880" cy="1556" r="60"/>
  </g>
  <g fill="var(--blue)">
    <circle cx="320" cy="1556" r="50"/><circle cx="600" cy="1678" r="50"/><circle cx="880" cy="1556" r="50"/>
  </g>
  <g fill="none" stroke="#fff" stroke-width="3">
    <rect x="298" y="1536" width="44" height="30" rx="2"/>
    <line x1="320" y1="1566" x2="320" y2="1576"/><line x1="308" y1="1577" x2="332" y2="1577"/>
    <circle cx="600" cy="1678" r="9"/>
    <line x1="600" y1="1669" x2="600" y2="1652"/><line x1="600" y1="1687" x2="600" y2="1704"/>
    <line x1="591" y1="1678" x2="574" y2="1678"/><line x1="609" y1="1678" x2="626" y2="1678"/>
    <line x1="607" y1="1671" x2="618" y2="1660"/><line x1="593" y1="1685" x2="582" y2="1696"/>
    <line x1="593" y1="1671" x2="582" y2="1660"/><line x1="607" y1="1685" x2="618" y2="1696"/>
    <ellipse cx="880" cy="1536" rx="16" ry="5"/>
    <path d="M864 1536v28c0 3 7 5 16 5s16-2 16-5v-28M864 1545c0 3 7 5 16 5s16-2 16-5M864 1555c0 3 7 5 16 5s16-2 16-5"/>
  </g>
  <g fill="#fff">
    <circle cx="600" cy="1652" r="4"/><circle cx="600" cy="1704" r="4"/><circle cx="574" cy="1678" r="4"/><circle cx="626" cy="1678" r="4"/>
    <circle cx="618" cy="1660" r="4"/><circle cx="582" cy="1696" r="4"/><circle cx="582" cy="1660" r="4"/><circle cx="618" cy="1696" r="4"/>
  </g>
</svg>

<div class="step-title" style="left:600px;top:1523px">Investment Process</div>
<div class="step-text" style="left:600px;top:1553px">Class aptent taciti sociosqu ad litora torquent per conubia nostra per inceptos hymenaeos</div>
<div class="step-title" style="left:318px;top:1637px">Sign Up with Us</div>
<div class="step-text" style="left:318px;top:1668px">Class aptent taciti sociosqu ad litora torquent per conubia nostra per inceptos hymenaeos</div>
<div class="step-title" style="left:882px;top:1642px">Make Money</div>
<div class="step-text" style="left:882px;top:1672px">Class aptent taciti sociosqu ad litora torquent per conubia nostra per inceptos hymenaeos</div>

<section class="investors">
  <h2>Our Investors</h2>
  <span class="partner" style="left:268px;top:144px">Quillarn</span>
  <span class="partner" style="left:398px;top:144px">Torvessa</span>
  <span class="partner" style="left:524px;top:144px">Pellinor</span>
  <span class="partner" style="left:661px;top:144px">Zarnhold</span>
  <span class="partner" style="left:798px;top:144px">Vexmoor</span>
  <span class="partner" style="left:933px;top:144px">Ulvra</span>
  <span class="partner" style="left:268px;top:217px">Brennick</span>
  <span class="partner" style="left:398px;top:217px">Osterlyn</span>
  <span class="partner" style="left:524px;top:217px">Kelvarro</span>
  <span class="partner" style="left:661px;top:217px">Thistrand</span>
  <span class="partner" style="left:798px;top:217px">Yarrowick</span>
  <span class="partner" style="left:933px;top:217px">Quenby</span>
</section>

<h2 class="section-title" style="top:2160px">Testimonials</h2>
<div class="portrait" role="img" aria-label="Portrait photo of the client giving the testimonial"></div>
<span class="quote-mark" style="left:398px;top:2222px">“</span>
<p class="quote-text">Maecenas aliquet velit vel turpis Mauris neque metus malesuada nec ultricies sit amet porttitor mattis enim In massa libero interdum nec interdum vel blandit sed nulla In ullamcorper</p>
<span class="quote-mark" style="left:765px;top:2296px">”</span>
<div class="author">By Author Name</div>
<div class="city">City Location</div>

<footer class="site-footer">
  <div class="footer-col" style="left:193px">
    <h4>QUICK LINKS</h4>
    <ul><li>Home</li><li>About Us</li><li>Our Services</li><li>Testimonials</li><li>Partners</li></ul>
  </div>
  <div class="footer-col" style="left:381px">
    <h4>RESOURCES</h4>
    <ul><li>Broker</li><li>Projects</li><li>Team</li><li>Our Blogs</li></ul>
  </div>
  <div class="footer-col" style="left:561px">
    <h4>CONTACT INFO</h4>
    <ul><li>410 Harbor Point Road Suite</li><li>B12 Fairhaven, PA 19210</li><li>(555) 318-4400</li><li>hello@brightfoldcapital.example</li></ul>
  </div>
  <div class="footer-brand"><span class="brand-dot"></span>BRIGHTFOLD CAPITAL</div>
  <div class="footer-rule"></div>
  <div class="footer-bottom" style="left:187px">© 2016 Company Name  All right reserved</div>
  <div class="footer-bottom" style="right:193px">Privacy policy &amp; Terms of Use</div>
</footer>

</body>
</html>
```